Halvern Mechanical Contractors needs a Website

Create basic website for commercial plumbing and mechanical contractor; to include pictures of works in progress and completed works, description of all services offered and geographical locations and licenses

Target Market(s)

General Contractors, Real Estate Developers, Construction Companies

Industry/Entity Type

Construction

Coding

Coded - Design and coding required

Number of Pages Required

5+ page

Font styles to use
Other font styles liked:
• See logo attached to project

Colors
0392cd

```html
<!DOCTYPE html>
<html lang="en">
<head>
<meta charset="utf-8">
<title>Halvern Mechanical Contractors</title>
<link rel="stylesheet" href="https://fonts.googleapis.com/css2?family=Lato:wght@400;700;900&family=Mulish:wght@600;700;800&display=swap">
<style>
:root{
  --brand:#0392cd;
  --navy:#1d3a5f;
  --ink:#1a1a1a;
  --text:#333;
  --grey-bg:#ebebeb;
  --dark:#1b1b1b;
  --footer:#2e2e2e;
  --white:#fff;
  --muted:#8a8a8a;
}
*{box-sizing:border-box;margin:0;padding:0}
html,body{width:1200px;height:2699px;overflow:hidden}
body{font-family:"Lato",sans-serif;color:var(--text);background:var(--white);position:relative}
.abs{position:absolute}
.topbar{left:0;top:0;width:1200px;height:45px;background:#000;color:var(--white);font-size:14px}
.topbar .item{position:absolute;top:8px;display:flex;align-items:center;gap:10px}
.topbar .dot{width:30px;height:30px;border-radius:50%;background:var(--brand);display:flex;align-items:center;justify-content:center}
.header{left:0;top:45px;width:1200px;height:101px;background:var(--white)}
.brand{position:absolute;left:56px;top:14px;display:flex;align-items:center;gap:12px}
.brand .mark{width:72px;height:72px;border-radius:50%;background:var(--navy)}
.brand .name{font-family:"Mulish",sans-serif;font-weight:800;color:var(--navy);font-size:21px;line-height:22px;text-transform:uppercase}
.nav a{position:absolute;top:0;height:101px;line-height:101px;font-size:16px;color:var(--ink);text-decoration:none}
.nav a.active{background:#000;color:var(--white);width:92px;left:497px;text-align:center;font-weight:700}
.hero{left:0;top:146px;width:1200px;height:514px;background:linear-gradient(135deg,#b9b7b2 0%,#e8e6e1 35%,#d4d2cd 55%,#c98a5c 80%,#8c5a3a 100%)}
.hero-arrow{position:absolute;top:256px;width:28px;height:28px;border:2px solid var(--white);background:rgba(0,0,0,.25)}
.tagline{left:0;top:660px;width:1200px;height:65px;background:var(--brand);color:var(--white);font-weight:900;font-size:29px;text-align:center;line-height:65px;letter-spacing:.2px}
.section-title{position:absolute;left:0;width:1200px;text-align:center;font-family:"Mulish",sans-serif;font-weight:800;font-size:31px;color:var(--ink)}
.section-title span{color:var(--brand)}
.rule{position:absolute;left:392px;width:416px;height:1px;background:#c8c8c8}
.about-title{color:var(--navy)}
.about-title span{color:var(--muted)}
.about-copy{left:70px;top:832px;width:1060px;text-align:center;font-size:14px;line-height:28px;color:var(--text)}
.btn{left:525px;top:972px;width:157px;height:40px;border-radius:20px;background:var(--brand);color:var(--white);font-weight:900;font-size:15px;line-height:40px;padding-left:20px}
.btn i{position:absolute;right:5px;top:5px;width:30px;height:30px;border-radius:50%;background:var(--white)}
.services{left:0;top:1056px;width:1200px;height:405px;background:var(--grey-bg)}
.service{position:absolute;top:1170px;width:210px;text-align:center}
.service .icon{width:108px;height:108px;margin:20px auto 0;border-radius:50%;background:linear-gradient(180deg,#c9d6e2,#e1e5ea);border:10px solid #d6dbe0}
.service h3{margin-top:30px;font-size:18px;color:var(--brand);font-weight:700}
.service p{margin-top:6px;font-size:14px;line-height:20px;color:var(--ink)}
.service p b{color:var(--brand);font-weight:400}
.gallery{left:0;top:1461px;width:1200px;height:514px;background:radial-gradient(ellipse at 50% 40%,#3a3a3a,#141414 75%)}
.tab{position:absolute;top:1594px;width:184px;height:38px;line-height:36px;text-align:center;font-size:17px;color:var(--white);border:2px solid var(--white)}
.tab.current{background:#8a8a8a;border-color:#8a8a8a}
.tab.current:after{content:"";position:absolute;left:82px;bottom:-10px;border:9px solid transparent;border-bottom:0;border-top-color:#8a8a8a}
.photo{position:absolute}
.g-arrow{position:absolute;top:1762px;width:34px;height:34px;border-radius:50%;border:1px solid #999}
.reviews-quote{left:190px;top:2090px;width:820px;text-align:center;font-size:14px;line-height:28px;color:var(--ink)}
.qmark{position:absolute;top:2080px;font-family:"Mulish",sans-serif;font-size:120px;line-height:120px;color:#c6c6c6;font-weight:800}
.reviewer{left:0;top:2194px;width:1200px;text-align:center;color:var(--brand);font-weight:700;font-size:16px}
.avatar{position:absolute;top:2240px;width:97px;height:97px;border-radius:50%;border:3px solid #ddd;background:linear-gradient(180deg,#d9cfc6,#9da6ae)}
.avatar.active{border-color:var(--navy)}
.pager{position:absolute;top:2373px;width:11px;height:11px;background:#ccc}
.footer{left:0;top:2425px;width:1200px;height:227px;background:var(--footer);color:var(--white)}
.f-head{position:absolute;top:2442px;font-weight:700;font-size:16px;color:var(--white)}
.f-line{position:absolute;top:2472px;height:1px;background:#555}
.links{position:absolute;left:65px;top:2477px;list-style:none;font-size:13.5px;color:var(--white)}
.links li{height:32px;line-height:32px;padding-left:12px;position:relative}
.links li:before{content:"";position:absolute;left:0;top:12px;border:4px solid transparent;border-left:5px solid var(--white);border-right:0}
.contact{position:absolute;left:297px;top:2483px;font-size:13.5px;list-style:none;color:var(--white)}
.contact li{position:relative;padding-left:26px;margin-bottom:12px;line-height:20px}
.contact svg{position:absolute;left:0;top:2px}
.map{left:666px;top:2491px;width:257px;height:139px;border:4px solid var(--white);background:linear-gradient(135deg,#eae6dc,#d8d4c8)}
.f-brand{position:absolute;left:1006px;top:2470px;width:150px;text-align:center;font-family:"Mulish",sans-serif;font-weight:800;font-size:17px;line-height:20px;color:#777;text-transform:uppercase}
.f-brand .c{display:block;width:70px;height:70px;border-radius:50%;background:#555;margin:0 auto 12px}
.copy{left:0;top:2652px;width:1200px;height:47px;background:var(--brand);color:var(--white);font-weight:700;font-size:14px;line-height:47px;padding-left:65px}
.social{position:absolute;top:2662px;width:28px;height:28px;border-radius:50%;background:var(--white)}
</style>
</head>
<body>

<div class="abs topbar">
  <div class="item" style="left:734px">
    <span class="dot"><svg width="14" height="14" viewBox="0 0 24 24"><path fill="#fff" d="M6.6 10.8a15 15 0 006.6 6.6l2.2-2.2a1 1 0 011-.25 11.4 11.4 0 003.6.57 1 1 0 011 1V20a1 1 0 01-1 1A17 17 0 013 4a1 1 0 011-1h3.5a1 1 0 011 1c0 1.25.2 2.45.57 3.6a1 1 0 01-.25 1z"/></svg></span>123 456 7890</div>
  <div class="item" style="left:884px">
    <span class="dot"><svg width="14" height="12" viewBox="0 0 24 18"><path fill="#fff" d="M0 0h24v18H0z"/><path fill="none" stroke="#0392cd" stroke-width="2" d="M0 1l12 9 12-9"/></svg></span>inquiry@halvernmechanical.com</div>
</div>

<header class="abs header">
  <div class="brand"><span class="mark"></span><span class="name">Halvern<br>Mechanical<br>Contractors</span></div>
  <nav class="nav">
    <a class="active" href="#">Home</a>
    <a href="#" style="left:622px">About Us</a>
    <a href="#" style="left:742px">Our Services</a>
    <a href="#" style="left:890px">Project Gallery</a>
    <a href="#" style="left:1054px">Contact Us</a>
  </nav>
</header>

<div class="abs hero" role="img" aria-label="Photo of copper pipe fittings, braided hoses and a wrench lying on plumbing blueprints">
  <span class="hero-arrow" style="left:18px"></span>
  <span class="hero-arrow" style="left:1152px"></span>
</div>
<div class="abs tagline">WE ARE A &nbsp;COMMERCIAL PLUMBING &amp; MECHANICAL CONTRACTOR</div>

<h2 class="section-title about-title" style="top:760px">About Halvern Mechanical <span>Contractors</span></h2>
<div class="rule" style="top:808px"></div>
<p class="abs about-copy">Lorem ipsum dolor sit amet, consectetuer adipiscing elit, sed diam nonummy nibh euismod tincidunt ut laoreet dolore magna aliquam erat volutpat. Ut wisi enim ad minim veniam, quis nostrud exerci tation ullamcorper suscipit lobortis nisl ut aliquip ex ea commodo consequat. Duis autem vel eum iriure dolor in hendrerit in vulputate velit esse molestie consequat, vel illum dolore eu feugiat nulla facilisis at vero eros et accumsan et iusto odio dignissim qui blandit praesent luptatum zzril delenit augue duis dolore te feugait nulla facilisi.</p>
<a class="abs btn">READ MORE<i></i></a>

<section class="abs services"></section>
<h2 class="section-title" style="top:1089px">Our <span>Services</span></h2>
<div class="rule" style="top:1146px"></div>
<div class="service" style="left:52px"><div class="icon" role="img" aria-label="Drain services icon"></div><h3>Drain Services</h3><p>Lorem ipsum dolor sit amet,<br>consectetuer adipis <b>...[+]</b></p></div>
<div class="service" style="left:273px"><div class="icon" role="img" aria-label="Plumbing services icon"></div><h3>Plumbing Services</h3><p>Lorem ipsum dolor sit amet,<br>consectetuer adipis <b>...[+]</b></p></div>
<div class="service" style="left:494px"><div class="icon" role="img" aria-label="Water restoration icon"></div><h3>Water Restoration</h3><p>Lorem ipsum dolor sit amet,<br>consectetuer adipis <b>...[+]</b></p></div>
<div class="service" style="left:715px"><div class="icon" role="img" aria-label="HVAC systems icon"></div><h3>HVAC Systems</h3><p>Lorem ipsum dolor sit amet,<br>consectetuer adipis <b>...[+]</b></p></div>
<div class="service" style="left:937px"><div class="icon" role="img" aria-label="Emergency services icon"></div><h3>Emergency Services</h3><p>Lorem ipsum dolor sit amet,<br>consectetuer adipis <b>...[+]</b></p></div>

<section class="abs gallery" role="img" aria-label="Dark blurred background of pipework"></section>
<h2 class="section-title" style="top:1492px;color:var(--white)">Project Gallery</h2>
<div class="rule" style="top:1551px;background:#666"></div>
<span class="tab" style="left:401px">Progress Works</span>
<span class="tab current" style="left:613px">Completed Works</span>

<div class="photo" style="left:242px;top:1733px;width:195px;height:183px;background:linear-gradient(160deg,#6c7a88,#2b3440)" role="img" aria-label="Worker using a power drill"></div>
<div class="photo" style="left:424px;top:1694px;width:196px;height:183px;background:linear-gradient(160deg,#c9ccce,#7d8388)" role="img" aria-label="Industrial pipework and valves"></div>
<div class="photo" style="left:593px;top:1733px;width:196px;height:183px;background:linear-gradient(160deg,#d7d9d8,#8b8f8a)" role="img" aria-label="Workers in a plant room"></div>
<div class="photo" style="left:763px;top:1694px;width:196px;height:183px;background:linear-gradient(160deg,#a5b5c6,#2d5c99)" role="img" aria-label="Technician in blue overalls"></div>
<div class="photo" style="left:930px;top:1733px;width:196px;height:183px;background:linear-gradient(160deg,#9aa7b3,#2a4f80)" role="img" aria-label="Worker holding blue hoses"></div>
<div class="photo" style="left:72px;top:1688px;width:195px;height:182px;background:linear-gradient(160deg,#4d5866,#1d2530)" role="img" aria-label="Worker with a clipboard">
  <div style="position:absolute;top:54px;width:100%;text-align:center;color:#fff;font-weight:700;font-size:17px">Loren Ipsum Sit</div>
  <svg style="position:absolute;left:83px;top:92px" width="30" height="30" viewBox="0 0 30 30"><circle cx="15" cy="15" r="13" fill="none" stroke="#fff" stroke-width="2"/><path d="M15 8v14M8 15h14" stroke="#fff" stroke-width="2"/></svg>
</div>
<span class="g-arrow" style="left:20px"></span>
<span class="g-arrow" style="left:1144px"></span>

<h2 class="section-title" style="top:2008px">Customer <span>Reviews</span></h2>
<div class="rule" style="top:2066px"></div>
<span class="qmark" style="left:124px">“</span>
<span class="qmark" style="left:1016px">”</span>
<p class="abs reviews-quote">Fusce elementum, nulla vel pellentes consequat, ante nulla hendrerit arcu, ac tincidunt mauris lacus sed leo. vamus suscipit molestie vestibulum. Lorem ipsum dolor sit amet, Fusce elementum, nulla vel pellentes consequat, ante nulla hendrerit arcu, ac tincidunt mauris lacus sed leo. vamus suscipit molestie. Fusce elementum, nulla vel</p>
<div class="abs reviewer">Marisol</div>
<span class="avatar" style="left:424px" role="img" aria-label="Customer portrait"></span>
<span class="avatar active" style="left:552px" role="img" aria-label="Customer portrait"></span>
<span class="avatar" style="left:681px" role="img" aria-label="Customer portrait"></span>
<span class="pager" style="left:577px;background:var(--brand)"></span>
<span class="pager" style="left:594px"></span>
<span class="pager" style="left:611px"></span>

<footer class="abs footer"></footer>
<div class="f-head" style="left:65px">Quick Links</div>
<div class="f-line" style="left:65px;width:144px"></div>
<ul class="links"><li>Home</li><li>About Us</li><li>Our Services</li><li>Project Gallery</li><li>Contact Us</li></ul>
<div class="f-head" style="left:297px">Contact Details</div>
<div class="f-line" style="left:297px;width:282px"></div>
<ul class="contact">
  <li><svg width="14" height="18" viewBox="0 0 14 18"><path fill="#fff" d="M7 0a7 7 0 00-7 7c0 5 7 11 7 11s7-6 7-11a7 7 0 00-7-7zm0 10a3 3 0 110-6 3 3 0 010 6z"/></svg>Lorem ipsum dolor sit amet, con<br>adipiscing elit - 123456</li>
  <li><svg width="15" height="15" viewBox="0 0 24 24"><path fill="#fff" d="M6.6 10.8a15 15 0 006.6 6.6l2.2-2.2a1 1 0 011-.25 11.4 11.4 0 003.6.57 1 1 0 011 1V20a1 1 0 01-1 1A17 17 0 013 4a1 1 0 011-1h3.5a1 1 0 011 1c0 1.25.2 2.45.57 3.6a1 1 0 01-.25 1z"/></svg>123 456 7890</li>
  <li><svg width="15" height="15" viewBox="0 0 24 24"><path fill="#fff" d="M6.6 10.8a15 15 0 006.6 6.6l2.2-2.2a1 1 0 011-.25 11.4 11.4 0 003.6.57 1 1 0 011 1V20a1 1 0 01-1 1A17 17 0 013 4a1 1 0 011-1h3.5a1 1 0 011 1c0 1.25.2 2.45.57 3.6a1 1 0 01-.25 1z"/></svg>123 456 7890</li>
  <li><svg width="15" height="12" viewBox="0 0 24 18"><path fill="#fff" d="M0 0h24v18H0z"/><path fill="none" stroke="#2e2e2e" stroke-width="2" d="M0 1l12 9 12-9"/></svg>info@halvernmechanical.com</li>
</ul>
<div class="f-head" style="left:666px">Location Map</div>
<div class="f-line" style="left:666px;width:254px"></div>
<div class="abs map" role="img" aria-label="Street map showing the office location"></div>
<div class="f-brand"><span class="c"></span>Halvern Mechanical Contractors</div>

<div class="abs copy">Copyright © 2016 Halvern Mechanical Contractors. All Right Reserved.</div>
<span class="social" style="left:1044px"></span>
<span class="social" style="left:1078px"></span>
<span class="social" style="left:1112px"></span>

</body>
</html>
```